Business card design for Tolvin Waste

I would like double-sided business cards for myself and my partner that includes our logo and the existing colour scheme. We provide waste and environmental services to customers in the motor-vehicle and engineering industries.

```html
<!DOCTYPE html>
<html lang="en">
<head>
<meta charset="utf-8">
<title>Tolvin Waste — Business Card</title>
<link href="https://fonts.googleapis.com/css2?family=Montserrat:wght@400;500;700&family=Oswald:wght@600&display=swap" rel="stylesheet">
<style>
  :root {
    --page: #e9e8e6;
    --card-dark-1: #4a4b4d;
    --card-dark-2: #2f3032;
    --ink: #3d3e40;
    --ink-soft: #5a5b5d;
    --green: #7cb342;
    --green-light: #a5d04b;
    --swoosh-grey: #4b4c4e;
    --white: #ffffff;
    --faint: #f0f0f0;
  }
  * { box-sizing: border-box; margin: 0; padding: 0; }
  html, body { width: 1200px; height: 930px; overflow: hidden; }
  body {
    background: var(--page);
    font-family: "Montserrat", sans-serif;
    position: relative;
  }
  .card {
    position: absolute;
    left: 290px;
    width: 620px;
    height: 354px;
    border-radius: 16px;
    overflow: hidden;
    box-shadow: 0 6px 18px rgba(0,0,0,0.18);
  }

  /* Back side */
  .card-back {
    top: 70px;
    background: linear-gradient(135deg, var(--card-dark-1), var(--card-dark-2));
  }
  .card-back .brand {
    position: absolute;
    left: 0; right: 0;
    top: 128px;
    display: flex;
    justify-content: center;
    align-items: center;
    gap: 16px;
  }
  .brand-dot {
    width: 46px; height: 46px;
    border-radius: 50%;
    background: var(--green);
    flex: none;
  }
  .brand-name {
    font-family: "Montserrat", sans-serif;
    font-weight: 700;
    font-size: 40px;
    letter-spacing: 1px;
    text-transform: uppercase;
    line-height: 1;
    white-space: nowrap;
  }
  .card-back .brand-name { color: #5c5d60; }
  .card-back .website {
    position: absolute;
    left: 0; right: 0;
    top: 232px;
    text-align: center;
    color: #e6e6e6;
    font-size: 17px;
    letter-spacing: 2px;
  }

  /* Front side */
  .card-front {
    top: 500px;
    background: var(--white);
  }
  .card-front .watermark {
    position: absolute;
    right: 60px; top: 24px;
    width: 250px; height: 250px;
    border-radius: 50%;
    border: 26px solid var(--faint);
  }
  .card-front .brand {
    position: absolute;
    left: 40px; top: 92px;
    display: flex;
    align-items: center;
    gap: 10px;
  }
  .card-front .brand-dot { width: 34px; height: 34px; }
  .card-front .brand-name { font-size: 24px; color: var(--ink); }

  .holder {
    position: absolute;
    right: 64px; top: 62px;
    text-align: right;
  }
  .holder-name {
    font-family: "Oswald", sans-serif;
    font-weight: 600;
    font-size: 30px;
    color: var(--green);
    text-transform: uppercase;
    line-height: 1;
    white-space: nowrap;
  }
  .holder-role {
    font-size: 15px;
    color: var(--ink-soft);
    margin-top: 2px;
  }

  .contact {
    position: absolute;
    left: 96px; top: 168px;
    color: var(--ink);
    font-size: 15px;
    line-height: 1.3;
  }
  .address { margin-bottom: 10px; }
  .contact-line { display: flex; align-items: center; gap: 8px; }
  .contact-line svg { width: 12px; height: 12px; flex: none; }
  .accent { color: var(--green); }

  .swoosh {
    position: absolute;
    left: 0; bottom: 0;
    width: 620px; height: 150px;
  }
</style>
</head>
<body>

  <section class="card card-back" aria-label="Card back">
    <div class="brand">
      <span class="brand-dot"></span>
      <span class="brand-name">Tolvin Waste</span>
    </div>
    <p class="website">www.tolvinwaste.com</p>
  </section>

  <section class="card card-front" aria-label="Card front">
    <div class="watermark"></div>

    <div class="brand">
      <span class="brand-dot"></span>
      <span class="brand-name">Tolvin Waste</span>
    </div>

    <div class="holder">
      <p class="holder-name">Corin Maddox</p>
      <p class="holder-role">Director</p>
    </div>

    <div class="contact">
      <p class="address">42 Wattlebrook Street<br>KELDRA NSW 2790</p>
      <p class="contact-line">
        <svg viewBox="0 0 12 12"><path d="M2 1l2.5 0 1 3-1.5 1a6 6 0 0 0 3 3l1-1.5 3 1V10a1 1 0 0 1-1 1A9 9 0 0 1 1 2a1 1 0 0 1 1-1z" fill="#7cb342"/></svg>
        <span>(123) 555-0147</span>
      </p>
      <p class="contact-line">
        <svg viewBox="0 0 12 12"><rect x="1" y="2.5" width="10" height="7" rx="1" fill="none" stroke="#7cb342" stroke-width="1.3"/><path d="M1.5 3l4.5 3.5L10.5 3" fill="none" stroke="#7cb342" stroke-width="1.3"/></svg>
        <span>info@tolvinwaste.com</span>
      </p>
      <p class="contact-line">
        <svg viewBox="0 0 12 12"><circle cx="6" cy="6" r="5" fill="#7cb342"/><path d="M1 6h10M6 1c-2.5 3-2.5 7 0 10M6 1c2.5 3 2.5 7 0 10" fill="none" stroke="#fff" stroke-width="0.8"/></svg>
        <span>www.<span class="accent">tolvinwaste</span>.com</span>
      </p>
    </div>

    <svg class="swoosh" viewBox="0 0 620 150" preserveAspectRatio="none" aria-hidden="true">
      <path d="M0 112 C160 72 340 90 470 58 C540 40 590 20 620 8 L620 150 L0 150 Z" fill="#a5d04b"/>
      <path d="M0 120 C170 84 340 100 470 68 C540 50 590 30 620 18 L620 150 L0 150 Z" fill="#7cb342"/>
      <path d="M0 128 C180 96 350 110 480 80 C545 64 595 42 620 32 L620 150 L0 150 Z" fill="#ffffff"/>
      <path d="M0 136 C190 104 360 118 490 90 C550 76 598 56 620 46 L620 150 L0 150 Z" fill="#4b4c4e"/>
    </svg>
  </section>

</body>
</html>
```